Health and Wellness Company Business Card

I need a business card design that is clean and uses modern minimalist style. The design should incorporate our logo (see attached). I would also like to use embossing on the cards so that they also have a great feel. I am open to the card using one or more colors, and these do not have to correspond to the colors in the concept paper. The card can either be one-sided or use both sides of the card.The logo uses the Avenir font.

I will need the file designed in Adobe CS and compatible with CS5.5 (Illustrator preferable) and I'll need the working file (for example: .ai) once the project is complete so that I can change the names/contact info/etc for each variation of the card.

This needs to be a memorable card for the recipient. They should think: "This is a great business card" either because of its simplicity or embossing effects or use of color.

Target Market(s)

The audience for our company has two main groups: people who pay for healthcare (insurers, companies, researcher companies) and people with chronic health conditions who are the consumers of our services and resources.

Industry/Entity Type

Business

Requirements
Must have
• Essential components of the card include: Company logo, contact Name (Mark Tolley), phone number (5808127346), email address (mtolley@brenquora.com), slogan/tagline that consists of ~30-40 characters (Use Lorem Ipsum)
Nice to have
• These fall just slightly short of "must have" to allow for design flexibility: Embossing or spot varnish effects and a splash of color
Should not have
• Designs with these components will not be successful: flashy or showy designs that are not professional in appearance, and lots of different colors

```html
<!DOCTYPE html>
<html lang="en">
<head>
<meta charset="utf-8">
<title>Brenquora – Business Card</title>
<link href="https://fonts.googleapis.com/css2?family=Mulish:wght@300;400&display=swap" rel="stylesheet">
<style>
  :root {
    --paper: #ffffff;
    --frame: #3d4a52;
    --slate: #7b7b8c;
    --slate-light: #8a8a9a;
    --teal-dark: #3a525a;
    --ink: #1c1c1f;
  }
  * { margin: 0; padding: 0; box-sizing: border-box; }
  html, body {
    width: 1200px;
    height: 720px;
    overflow: hidden;
    background: var(--paper);
  }
  .card {
    position: relative;
    width: 1200px;
    height: 720px;
    background: var(--paper);
    border: 1.5px solid var(--frame);
    font-family: "Mulish", "Avenir", sans-serif;
  }
  .card__divider {
    position: absolute;
    left: 688px;
    top: 0;
    width: 2px;
    height: 100%;
    background: var(--teal-dark);
  }
  .card__tab {
    position: absolute;
    left: 688px;
    top: 132px;
    width: 38px;
    height: 72px;
    background: var(--teal-dark);
    border-radius: 0 10px 10px 0;
  }

  /* Brand side */
  .brand__mark {
    position: absolute;
    left: 286px;
    top: 226px;
    width: 120px;
    height: 120px;
    background: var(--slate);
  }
  .brand__name {
    position: absolute;
    left: 62px;
    top: 414px;
    font-size: 64px;
    font-weight: 400;
    letter-spacing: 19px;
    color: var(--slate);
    text-transform: uppercase;
    line-height: 1;
    white-space: nowrap;
  }
  .brand__tagline {
    position: absolute;
    left: 89px;
    top: 534px;
    font-size: 28px;
    font-weight: 300;
    letter-spacing: 3.6px;
    word-spacing: 5px;
    line-height: 1.2;
    color: var(--slate-light);
    white-space: nowrap;
  }

  /* Contact side */
  .contact__name {
    position: absolute;
    left: 776px;
    top: 278px;
    font-size: 42px;
    font-weight: 300;
    color: var(--ink);
    white-space: nowrap;
  }
  .contact__row {
    position: absolute;
    display: flex;
    align-items: center;
    white-space: nowrap;
    color: var(--ink);
    font-weight: 300;
  }
  .contact__row--phone {
    left: 736px;
    top: 334px;
    font-size: 31px;
  }
  .contact__row--phone .contact__icon { margin-right: 22px; }
  .contact__row--email {
    left: 722px;
    top: 538px;
    font-size: 27px;
    letter-spacing: 3.3px;
  }
  .contact__row--email .contact__icon { margin-right: 22px; }
  .contact__icon { flex: none; display: block; }
</style>
</head>
<body>
  <main class="card">
    <div class="card__divider"></div>
    <div class="card__tab"></div>

    <section class="brand">
      <div class="brand__mark"></div>
      <h1 class="brand__name">brenquora</h1>
      <p class="brand__tagline">Lorem Ipsum Dolor Amet</p>
    </section>

    <section class="contact">
      <h2 class="contact__name">Mark Tolley</h2>
      <p class="contact__row contact__row--phone">
        <svg class="contact__icon" width="20" height="36" viewBox="0 0 20 36" aria-hidden="true">
          <rect x="1.5" y="1.5" width="17" height="33" rx="3" fill="none" stroke="#7b7b8c" stroke-width="2.2"/>
          <line x1="4" y1="28" x2="16" y2="28" stroke="#7b7b8c" stroke-width="1.6"/>
        </svg>
        <span>5808127346</span>
      </p>
      <p class="contact__row contact__row--email">
        <svg class="contact__icon" width="34" height="24" viewBox="0 0 34 24" aria-hidden="true">
          <rect x="1.5" y="1.5" width="31" height="21" fill="none" stroke="#7b7b8c" stroke-width="2.4"/>
          <polyline points="1.5,1.5 17,14 32.5,1.5" fill="none" stroke="#7b7b8c" stroke-width="2.4"/>
        </svg>
        <span>mtolley@brenquora.com</span>
      </p>
    </section>
  </main>
</body>
</html>
```